Award winning pet photographer needs business card and letterhead

Business card and letterhead for our Pet photography business. We specialize in studio portraits of dogs.

Target Market(s)

Wealthy and middle class dog owners who would like photos of their dogs as wall art.

Industry/Entity Type

Portrait Photography

Contact Information for Business Card

Our business name is Tails of Glee Pet Photography. Would be good to include dog and a heart, bright colours and a modern design

Font styles to use
Sans Serif

Colors
f04a50
f68d4d
faa54b
33a6d7
33b8a4
abd036

Requirements
Must have
• Business name: Tails of Glee Pet Photography
• Phone number: 0437 560914
• Email: marcus@kfstudio.com.au
• Website:www.tailsofglee.com.au
• Photographer: Marcus Fenwick
Nice to have
• In Addition letterhead should include
• Studio address 27 Wren Close, Marrowdale 6015
• Postal Address 9 Harlow St, East Marrowdale 6015

```html
<!DOCTYPE html>
<html lang="en">
<head>
<meta charset="utf-8">
<title>Tails of Glee Pet Photography – Business Card</title>
<link rel="stylesheet" href="https://fonts.googleapis.com/css2?family=Source+Sans+3:wght@400;600&display=swap">
<style>
  :root {
    --backdrop: #1b1b1b;
    --card-front: #f3f3f3;
    --card-back: #33a6d7;
    --brand-blue: #33a6d7;
    --brand-orange: #f68d4d;
    --brand-teal: #33b8a4;
    --white: #ffffff;
  }
  * { margin: 0; padding: 0; box-sizing: border-box; }
  html, body {
    width: 1200px; height: 900px; overflow: hidden;
    background: var(--backdrop);
    font-family: "Source Sans 3", Arial, sans-serif;
  }
  .stage { position: relative; width: 1200px; height: 900px; }
  .card {
    position: absolute; top: 184px;
    width: 302px; height: 490px;
    border-radius: 12px;
    text-align: center;
  }
  .card--front { left: 299px; background: var(--card-front); }
  .card--back { left: 646px; width: 304px; background: var(--card-back); }

  .brand { position: absolute; top: 74px; left: 0; right: 0; }
  .brand__mark {
    display: block; margin: 0 auto 14px;
    width: 54px; height: 54px; border-radius: 50%;
    background: var(--brand-teal);
  }
  .brand__name {
    font-size: 30px; font-weight: 400; letter-spacing: 1px;
    text-transform: uppercase; color: var(--brand-teal); line-height: 1;
  }
  .brand__tagline {
    margin-top: 6px; font-size: 19px; font-weight: 400;
    color: var(--brand-teal);
  }

  .person { position: absolute; top: 286px; left: 0; right: 0; }
  .person__name { font-size: 17px; font-weight: 600; color: var(--brand-blue); line-height: 1.1; }
  .person__role { font-size: 14px; color: var(--brand-orange); line-height: 1.3; }

  .contact { position: absolute; top: 353px; left: 0; right: 0; list-style: none; }
  .contact li { font-size: 14px; color: var(--brand-orange); line-height: 17.5px; }

  .back-brand {
    position: absolute; top: 150px; left: 0; right: 0;
  }
  .back-brand__mark {
    display: block; margin: 0 auto 22px;
    width: 120px; height: 120px; border-radius: 50%;
    background: var(--white);
  }
  .back-brand__name {
    font-size: 30px; font-weight: 400; letter-spacing: 1px;
    text-transform: uppercase; color: var(--white);
  }
</style>
</head>
<body>
  <main class="stage">
    <section class="card card--front" aria-label="Business card front">
      <div class="brand">
        <span class="brand__mark"></span>
        <div class="brand__name">Tails of Glee</div>
        <div class="brand__tagline">Pet Photography</div>
      </div>
      <div class="person">
        <div class="person__name">Marcus Fenwick</div>
        <div class="person__role">Photographer</div>
      </div>
      <ul class="contact">
        <li>0437 560914</li>
        <li>marcus@kfstudio.com.au</li>
        <li>www.tailsofglee.com.au</li>
      </ul>
    </section>

    <section class="card card--back" aria-label="Business card back">
      <div class="back-brand">
        <span class="back-brand__mark"></span>
        <div class="back-brand__name">Tails of Glee</div>
      </div>
    </section>
  </main>
</body>
</html>
```